Designing a new homepage for www.Brindlework.net

WEBSITE: www.brindlework.net

ABOUT THE WEBSITE
The Brindlework.net (BWK) website contains a large directory of over 50,000 international trade service providers that is not valued enough on the homepage (HP). Currently from the HP, the site appears as a general site about imports and exports (international trade). As a result, it contradicts the purpose and experience of the site.
The website is new and original for international trade online: it is a tool to find the best experts and professionals that can help importers and exporters to implement their overseas operations.

Specifically:
a) An exporter who wants to sell in Italy can find on BWK: agents to distribute their products, a lawyer for reviewing contracts, translators to translate brochures and websites, an export consultant, etc. Various local providers that can help sell their products in Italy, a local provider (e.g. based in Italy) are generally more efficient and less costly than a supplier in the exporter’s home country

b) An importer who wants to buy in China will find purchasing agents who source products for third parties; logistics companies that store and ship merchandise; corporate quality control to ensure product quality before shipment, etc.; various local providers based in China to better organize its import operation.

BWK is therefore a very resourceful solution for SMEs who want to develop, improve and organize their international trade:
a) it significantly increases their ability to create new opportunities by using the services of a third party: export to a new country; import a new product
b) it allows them to optimize their purchases of services by seeking alternatives: find a less expensive carrier, a foreign lawyer challenged by a local lawyer

It is the perfect complement to cross border marketplaces (e.g. Quorvanta.com, fenwickmarts.com, zl48.com) which concentrate on the search for products (and of companies/counterparts) but:
a) help the user to import only, not really export
b) do not help implement the operations of exporting/importing from A to Z

Therefore, BWK offers a new way of “easy exporting” (or easy importing).

THE BRIEF

The objective of the project is to rethink the HP (and the site design) to highlight this experience: "export and import more successfully through 50,000+ service providers in over 100 countries”.
We have created a wireframe (see attached) of the structure we feel best meets this objective. What do you think? Do we meet it through our wireframe? Then, next step is to take this wireframe and create a clear design that really helps us to achieve our objective.

It is considered that the site captures the importers/exporters seeking to increase their exports or to better organize their imports (but we do not start from a priori that these users are looking for service providers).
The HP should highlight the importance of service providers addressing export markets or better organizing their imports; the "market analyses" of the site should act as a "knowledge resource", where the site offers more the main experience: if you want to export to a country you have any interest to first explore what the partners listed by BWK can provide.

Reason: We feel that we're seeing some interesting designs and would like to give current and even potential submissions more time. So far we have not seen the one that really strikes us, so perhaps more time is what we and the designers need! Thanks!

Target Market(s)

Importers, exporters, international trade service providers, foreign investors, etc

Industry/Entity Type

Lawyer

Requirements
Must have
• • Please use the current basic design elements of the website, including the logo, (www.brindlework.net). These include colors and fonts, etc. We only aim to change the HP and therefore, only implement a change to the header and footer of the whole site.
• Please find inspiration from our wireframes (attached), as they have been carefully thought about by our own team. However, should you feel the need to challenge the wireframes, please do so in your design, we're interested to see what you can present us.
• Our prime objective in terms of design: creating a more user-friendly interface on the HP to guide users into the rest of the website
• We already have a psd file based on the wireframes we’ve attached to the brief. If you would like this, so your job is easier (such as using same text as we have in the wireframes), let us know!

```html
<!DOCTYPE html>
<html lang="en">
<head>
<meta charset="utf-8">
<title>Brindlework.net – The Network for International Trade Services</title>
<link rel="stylesheet" href="https://fonts.googleapis.com/css2?family=Source+Sans+3:ital,wght@0,400;0,600;0,700;1,700&display=swap">
<style>
:root{
  --navy:#1c3c5f;
  --nav:#2b5787;
  --blue:#3a6ea8;
  --band:#3b69a6;
  --text:#4a5e78;
  --muted:#8a8f96;
  --grey-box:#d9d9d9;
  --footer:#d4d4d4;
  --btn:#a9b2bd;
  --white:#fff;
  --star:#3d6fb0;
  --star-off:#9aa5b3;
}
*{box-sizing:border-box;margin:0;padding:0}
html,body{width:1200px;height:2703px;overflow:hidden;background:var(--white)}
body{position:relative;font-family:"Source Sans 3",Arial,sans-serif;color:var(--text)}
.abs{position:absolute}

/* top bar */
.topbar{left:0;top:0;width:1200px;height:39px;background:var(--navy);color:#dfe7f1;font-size:16px}
.topbar .links{position:absolute;left:22px;top:9px;display:flex}
.topbar .links span{padding:0 14px;border-right:1px solid #7e93ad}
.topbar .links span:first-child{padding-left:0}
.topbar .links span:last-child{border-right:none}
.like{display:inline-flex;align-items:center;gap:5px;background:#e8edf5;color:var(--navy);font-size:13px;font-weight:700;padding:1px 7px;border-radius:2px;margin-left:6px}
.like i{width:11px;height:11px;background:var(--nav);display:inline-block}
.topbar .account{position:absolute;right:0;top:0;height:39px;width:330px;background:#4a5f78;display:flex;align-items:center;justify-content:center;font-size:16px}
.topbar .account span{padding:0 11px;border-right:1px solid #8b9bb0}
.topbar .account span:last-child{border-right:none}

/* brand */
.brand{left:26px;top:62px;display:flex;align-items:center;gap:10px}
.brand .dot{width:30px;height:30px;border-radius:50%;background:var(--nav)}
.brand .name{font-size:40px;font-weight:700;color:var(--nav);letter-spacing:2px}
.tagline{left:66px;top:112px;font-size:17px;color:var(--navy)}
.tagline b{font-weight:700}

/* nav */
.nav{left:0;top:152px;width:1200px;height:53px;background:linear-gradient(#36679b,#24507f);border-top:3px solid #5b86b8}
.nav .items{position:absolute;left:54px;top:14px;display:flex;gap:72px;color:#e8eef6;font-size:16px;letter-spacing:.3px}
.search{position:absolute;right:18px;top:8px;width:468px;height:34px;background:#fff;border-radius:2px;font-size:15px;color:#6b7480;padding:7px 12px}
.search svg{position:absolute;right:8px;top:7px}

/* hero */
.hero{left:0;top:205px;width:1200px;height:455px;background:linear-gradient(100deg,#2f6fb7 0%,#7fb1e2 30%,#a9c6de 48%,#5c7fa3 62%,#3b73b4 80%,#9cc3e6 100%)}
.hero-copy{left:6px;top:212px;color:var(--nav)}
.hero-copy h1{font-size:37px;font-weight:700}
.hero-copy h2{font-size:19px;font-weight:700;margin-top:2px}
.hero-copy ul{list-style:none;font-size:17px;margin-top:2px}
.hero-copy li{padding-left:20px;position:relative;line-height:20px}
.hero-copy li::before{content:"";position:absolute;left:4px;top:6px;width:9px;height:9px;border-radius:50%;background:var(--nav)}
.hero-arrows{left:44px;top:596px;width:134px;height:64px;background:rgba(190,210,232,.85);display:flex;align-items:center;justify-content:center;gap:12px}

/* start band */
.start{left:0;top:660px;width:1200px;height:101px;background:var(--band);color:#fff}
.start .title{position:absolute;left:22px;top:26px;font-size:41px;font-weight:700;font-style:italic;letter-spacing:.5px}
.start .select{position:absolute;left:238px;top:33px;width:258px;height:40px;background:#fff;color:var(--navy);font-size:16px;padding:9px 14px}
.select .caret{position:absolute;right:6px;top:8px;width:26px;height:24px;background:var(--nav);display:flex;align-items:center;justify-content:center}
.start .find{position:absolute;left:507px;top:42px;font-size:18px}
.check{position:absolute;top:36px;display:flex;align-items:center;gap:8px;font-size:27px}
.check i{width:24px;height:24px;background:#fff;border:2px solid #c9d3de;display:inline-flex;align-items:center;justify-content:center}
.go{position:absolute;left:1108px;top:30px;width:57px;height:48px;background:#4b7fbf;border:2px solid #cfe0f2;font-size:29px;font-weight:700;display:flex;align-items:center;justify-content:center}

/* country box */
.country{left:26px;top:789px;width:1152px;height:249px;background:var(--grey-box);border:1px solid #c8c8c8}
.country h3{position:absolute;left:86px;top:4px;font-size:30px;color:var(--blue);font-weight:700}
.country .tri{position:absolute;top:10px}
.country .divider{position:absolute;left:574px;top:62px;width:1px;height:164px;background:#b9b9b9}
.country .badge{position:absolute;left:40px;top:76px;width:88px;height:88px;border-radius:50%;background:#f2f2f2;border:3px solid #aab0b8}
.country .intro{position:absolute;left:136px;top:76px;width:330px;font-size:17px;line-height:20px;color:var(--blue)}
.country .site{position:absolute;left:136px;top:192px;font-size:17px;color:var(--blue)}
.country .want{position:absolute;left:340px;top:192px;font-size:17px;color:var(--blue)}
.country .discover{position:absolute;left:670px;top:16px;font-size:17px;color:var(--blue)}
.stat{position:absolute;top:54px;text-align:center;color:var(--blue)}
.stat .n{font-size:76px;line-height:84px}
.stat .l{font-size:21px}
.stat .s{font-size:12px;line-height:14px}

/* columns */
.col-title{font-size:30px;color:var(--blue);font-weight:400}
.dir-head{font-size:20px;color:var(--blue)}
.dir{left:26px;top:1197px;width:340px;list-style:none;font-size:15.5px;line-height:26.9px;color:var(--text)}
.dir li{padding-left:22px;position:relative}
.dir li::before{content:"";position:absolute;left:4px;top:10px;width:8px;height:8px;border-radius:50%;background:#9aa7b6}
.more{font-size:15px;color:var(--blue)}

.photo{width:137px;height:118px;background:linear-gradient(160deg,#8a5a46,#d9b09a 55%,#f4ece6)}
.speaker{font-size:16px;line-height:20px;color:var(--blue)}
.quote{font-size:12.5px;line-height:19px;color:#555}
.small{font-size:11px;color:var(--muted)}
.btn{background:var(--btn);color:#fff;font-size:15px;text-align:center;line-height:28px;height:28px}

.tip .t{font-size:16px;line-height:20px;color:var(--blue)}
.tip .d{font-size:14.5px;line-height:17px;color:var(--muted);width:250px}
.rating{display:flex;align-items:center;gap:2px;fill:var(--star)}
.rating .off{fill:var(--star-off)}
.rated{font-size:15px;color:var(--muted);margin-left:20px}

.provider .logo{position:absolute;left:0;top:0;width:96px;height:90px;border:1px solid #b8b8b8;background:#fff;display:flex;align-items:center;justify-content:center}
.provider .logo i{width:48px;height:48px;background:#6c6f73;display:block}
.provider .logo i.round{border-radius:50%;background:#fff;border:3px solid #6c6f73}
.provider .info{position:absolute;left:115px;top:4px;font-size:16.5px;line-height:20px;color:var(--blue)}
.provider .info em{font-style:normal;font-size:14px;line-height:16px;color:var(--muted);display:block;width:180px}
.provider .view{position:absolute;left:230px;top:80px;font-size:14px;color:var(--muted)}

.know li{list-style:none;font-size:16px;line-height:30px;color:var(--text);padding-left:26px;position:relative}
.know li::before{content:"";position:absolute;left:4px;top:12px;width:8px;height:8px;border-radius:50%;background:#9aa7b6}

/* partner strip */
.rule{height:1px;background:#9da3aa}
.partners{left:40px;top:2238px;width:1120px;display:flex;justify-content:space-between;align-items:center}
.partners i{display:block;background:#c4c8cd}

/* footer */
.footer{left:0;top:2357px;width:1200px;height:346px;background:var(--footer)}
.fcol{position:absolute;top:20px}
.fcol h4{font-size:22px;font-weight:400;color:var(--blue);margin-bottom:6px}
.fcol p{font-size:15.5px;line-height:29px;color:#7c8794}
.fcol p.sm{font-size:12px}
.follow p{display:flex;align-items:center;gap:10px;color:var(--blue);line-height:36px;font-size:16px}
.follow i{width:20px;height:20px;background:var(--nav);display:inline-block;border-radius:2px}
.copy{position:absolute;left:0;top:312px;width:1200px;text-align:center;font-size:12.5px;color:var(--blue)}
</style>
</head>
<body>
<svg width="0" height="0" class="abs" aria-hidden="true">
  <defs>
    <symbol id="star" viewBox="0 0 24 24"><path d="M12 1.5l3.2 6.9 7.3.8-5.5 5 1.6 7.3L12 17.8l-6.6 3.7 1.6-7.3-5.5-5 7.3-.8z"/></symbol>
    <symbol id="pdf" viewBox="0 0 24 30"><path d="M4 1h13l6 6v22H4z" fill="#fff" stroke="#b8b8b8"/><rect x="1" y="7" width="16" height="9" fill="#c9302c"/><rect x="8" y="19" width="11" height="7" fill="#c9302c"/></symbol>
  </defs>
</svg>

<!-- top bar -->
<header class="abs topbar">
  <nav class="links"><span>Home</span><span>About us</span><span>Take a tour</span><span>Advertise</span><span>Why Brindlework.net <span class="like"><i></i>Like</span></span></nav>
  <div class="account"><span>LOGIN</span><span>SIGN UP</span><span>LIST YOUR SERVICES</span></div>
</header>

<div class="abs brand"><span class="dot"></span><span class="name">Brindlework.net</span></div>
<div class="abs tagline">The Network for <b>International Trade Services</b></div>

<nav class="abs nav">
  <div class="items"><span>ALL TRADE SERVICES</span><span>LET US HELP YOU</span><span>BROWSE KNOWLEDGE</span></div>
  <div class="search">Search 20,000+content items &amp; 50,000+services providers...
    <svg width="22" height="22" viewBox="0 0 22 22"><circle cx="9" cy="9" r="6.5" fill="none" stroke="#3a4654" stroke-width="3"/><path d="M14 14l6 6" stroke="#3a4654" stroke-width="3.5" stroke-linecap="round"/></svg>
  </div>
</nav>

<!-- hero -->
<div class="abs hero" role="img" aria-label="Photograph of modern glass office towers against a blue sky"></div>
<section class="abs hero-copy">
  <h1>Improve your business overseas!</h1>
  <h2>Use the leverage of $1,000 + verified services providers:</h2>
  <ul>
    <li>Sales agents,market entry,customs services</li>
    <li>sourcing companies,freight forwarders,quality control</li>
    <li>Lawyers,accounting, expat services and more</li>
  </ul>
</section>
<div class="abs hero-arrows">
  <svg width="46" height="46" viewBox="0 0 46 46"><circle cx="23" cy="23" r="20" fill="none" stroke="#1c3c5f" stroke-width="3"/><path d="M27 13l-10 10 10 10" fill="none" stroke="#1c3c5f" stroke-width="4"/></svg>
  <svg width="46" height="46" viewBox="0 0 46 46"><circle cx="23" cy="23" r="20" fill="none" stroke="#1c3c5f" stroke-width="3"/><path d="M19 13l10 10-10 10" fill="none" stroke="#1c3c5f" stroke-width="4"/></svg>
</div>

<!-- start now -->
<section class="abs start">
  <div class="title">START NOW</div>
  <div class="select">Select your target country
    <span class="caret"><svg width="14" height="10" viewBox="0 0 14 10"><path d="M0 0h14L7 10z" fill="#fff"/></svg></span>
  </div>
  <div class="find">and find assistance to</div>
  <div class="check" style="left:678px"><i><svg width="18" height="16" viewBox="0 0 18 16"><path d="M2 8l5 5L16 2" fill="none" stroke="#2b5787" stroke-width="3"/></svg></i>Import</div>
  <div class="check" style="left:820px"><i></i>Export</div>
  <div class="check" style="left:952px"><i></i>Invest</div>
  <div class="go">GO</div>
</section>

<!-- country spotlight -->
<section class="abs country">
  <svg class="tri" style="left:14px" width="22" height="32" viewBox="0 0 22 32"><path d="M22 0v32L0 16z" fill="#9fb4cc"/></svg>
  <svg class="tri" style="left:1114px" width="22" height="32" viewBox="0 0 22 32"><path d="M0 0v32l22-16z" fill="#9fb4cc"/></svg>
  <h3>Want &nbsp;to export to South Africa ?</h3>
  <div class="badge"></div>
  <p class="intro">Meridel South Africa<br>Export Support<br>There is no one who loves pain itself, who seeks after it and wants to have it, simply because it is pain</p>
  <div class="site">WWW.meridelsa.com</div>
  <div class="want">Want your logo here?</div>
  <div class="divider"></div>
  <div class="discover">Discover 451 service providers to help you export including</div>
  <div class="stat" style="left:590px;width:190px"><div class="n">25</div><div class="l">Freight forwarders</div><div class="s">in South Africa<br>See all</div></div>
  <div class="stat" style="left:786px;width:200px"><div class="n">47</div><div class="l">Corparate Lawyers</div><div class="s">in South Africa<br>See all</div></div>
  <div class="stat" style="left:980px;width:170px"><div class="n">56</div><div class="l">Debt Collectors</div><div class="s">in South Africa<br>See all</div></div>
</section>

<!-- directory -->
<h3 class="abs col-title" style="left:50px;top:1056px">Browse our Directory</h3>
<div class="abs dir-head" style="left:26px;top:1106px">Services 200+</div>
<div class="abs dir-head" style="left:197px;top:1106px">Countries 100+</div>
<ul class="abs dir">
  <li>Freight Forwarders (7843)</li><li>Trading Companies (2489)</li><li>Corparate Law (975)</li><li>Investment Promotion (817)</li><li>Distributors (656)</li><li>Debt Collection (561)</li>
  <li>Freight Forwarders (7843)</li><li>Trading Companies (2489)</li><li>Corparate Law (975)</li><li>Investment Promotion (817)</li><li>Distributors (656)</li><li>Debt Collection (561)</li>
  <li>Freight Forwarders (7843)</li><li>Trading Companies (2489)</li><li>Corparate Law (975)</li><li>Investment Promotion (817)</li><li>Distributors (656)</li><li>Debt Collection (561)</li>
  <li>Freight Forwarders (7843)</li><li>Trading Companies (2489)</li><li>Corparate Law (975)</li><li>Investment Promotion (817)</li><li>Distributors (656)</li><li>Debt Collection (561)</li>
  <li>Freight Forwarders (7843)</li><li>Trading Companies (2489)</li><li>Corparate Law (975)</li><li>Investment Promotion (817)</li><li>Distributors (656)</li><li>Debt Collection (561)</li>
  <li>Freight Forwarders (7843)</li><li>Trading Companies (2489)</li><li>Corparate Law (975)</li><li>Investment Promotion (817)</li><li>Distributors (656)</li><li>Debt Collection (561)</li>
</ul>
<div class="abs more" style="left:248px;top:2168px">view all services</div>

<!-- testimonials -->
<h3 class="abs col-title" style="left:408px;top:1056px">What Importers / Exporters say</h3>
<div class="abs photo" style="left:411px;top:1112px" role="img" aria-label="Portrait photo of a sourcing services speaker"></div>
<div class="abs speaker" style="left:563px;top:1136px">Name of Speaker<br>Sourcing Services<br>Florida, The united states</div>
<p class="abs quote" style="left:411px;top:1236px;width:380px">Lorem Ipsum is simply dummy text of the printing and typesetting industry. Lorem Ipsum has been the industry's standard dummy text ever since the 1500s, when an unknown printer took a galley of type and scrambled it to make a type specimen book. It has survived not only five centuries, but also the leap into electronic typesetting, remaining essentially unchanged. It was popularised in the 1960s with the release of sheets containing Lorem Ipsum passages, and more recently with desktop publishing software including versions of Lorem Ipsum.</p>
<div class="abs photo" style="left:411px;top:1442px;background:linear-gradient(160deg,#6b4a34,#c99a78 55%,#efe3d7)" role="img" aria-label="Portrait photo of a second sourcing services speaker"></div>
<div class="abs speaker" style="left:563px;top:1464px">Name of Speaker<br>Sourcing Services<br>Florida, The united states</div>
<p class="abs quote" style="left:411px;top:1566px;width:380px">Lorem Ipsum is simply dummy text of the printing and typesetting industry. Lorem Ipsum has been the industry's standard dummy text ever since the 1500s, when an unknown printer took a galley of type and scrambled it to make a type specimen book. It has survived not only five centuries, but also the leap into electronic typesetting, remaining essentially unchanged. It was popularised in the 1960s with the release of sheets containing Lorem Ipsum passages, and more recently with desktop publishing software including versions of Lorem Ipsum.</p>
<div class="abs small" style="left:412px;top:1778px">See the benefits</div>
<div class="abs btn" style="left:680px;top:1770px;width:92px">Join for free</div>

<!-- tips -->
<h3 class="abs col-title" style="left:405px;top:1810px;font-size:29px">Business Tips By Experts</h3>

<div class="abs tip" style="left:425px;top:1860px"><div class="t">Business Administration</div><div class="d">Lorem ipsum is the dummy text of the content for printing text</div></div>
<div class="abs rating" style="left:545px;top:1922px"><svg width="24" height="24"><use href="#star"/></svg><svg width="24" height="24"><use href="#star"/></svg><svg width="24" height="24"><use href="#star"/></svg><svg width="24" height="24" class="off"><use href="#star"/></svg><svg width="24" height="24" class="off"><use href="#star"/></svg><span class="rated">Rated</span></div>
<svg class="abs" style="left:735px;top:1904px" width="30" height="38"><use href="#pdf"/></svg>

<div class="abs tip" style="left:425px;top:1968px"><div class="t">Business Administration</div><div class="d">Lorem ipsum is the dummy text of the content for printing text</div></div>
<div class="abs rating" style="left:545px;top:2030px"><svg width="24" height="24"><use href="#star"/></svg><svg width="24" height="24"><use href="#star"/></svg><svg width="24" height="24"><use href="#star"/></svg><svg width="24" height="24"><use href="#star"/></svg><svg width="24" height="24" class="off"><use href="#star"/></svg><span class="rated">Rated</span></div>
<svg class="abs" style="left:735px;top:2012px" width="30" height="38"><use href="#pdf"/></svg>

<div class="abs tip" style="left:425px;top:2076px"><div class="t">Business Administration</div><div class="d">Lorem ipsum is the dummy text of the content for printing text</div></div>
<div class="abs rating" style="left:545px;top:2138px"><svg width="24" height="24"><use href="#star"/></svg><svg width="24" height="24"><use href="#star"/></svg><svg width="24" height="24"><use href="#star"/></svg><svg width="24" height="24"><use href="#star"/></svg><svg width="24" height="24" class="off"><use href="#star"/></svg><span class="rated">Rated</span></div>
<svg class="abs" style="left:735px;top:2120px" width="30" height="38"><use href="#pdf"/></svg>

<div class="abs more" style="left:430px;top:2172px">Browse all content</div>
<div class="abs btn" style="left:643px;top:2170px;width:187px;font-size:17px">RECEIVE UPDATES</div>

<!-- providers -->
<h3 class="abs col-title" style="left:884px;top:1056px">New Service Providers</h3>
<div class="abs provider" style="left:843px;top:1114px;width:335px;height:100px"><div class="logo"><i></i></div><div class="info">Harrowgate Media Limited<br>Tax service in United Kingdom<em>Lorem ipsum is simply dummy text of the printing</em></div><div class="view">View profile</div></div>
<div class="abs provider" style="left:843px;top:1237px;width:335px;height:100px"><div class="logo"><i class="round"></i></div><div class="info">Harrowgate Media Limited<br>Tax service in United Kingdom<em>Lorem ipsum is simply dummy text of the printing</em></div><div class="view">View profile</div></div>
<div class="abs provider" style="left:843px;top:1360px;width:335px;height:100px"><div class="logo"><i></i></div><div class="info">Harrowgate Media Limited<br>Tax service in United Kingdom<em>Lorem ipsum is simply dummy text of the printing</em></div><div class="view">View profile</div></div>
<div class="abs provider" style="left:843px;top:1483px;width:335px;height:100px"><div class="logo"><i class="round"></i></div><div class="info">Harrowgate Media Limited<br>Tax service in United Kingdom<em>Lorem ipsum is simply dummy text of the printing</em></div><div class="view">View profile</div></div>
<div class="abs provider" style="left:843px;top:1606px;width:335px;height:100px"><div class="logo"><i class="round"></i></div><div class="info">Harrowgate Media Limited<br>Tax service in United Kingdom<em>Lorem ipsum is simply dummy text of the printing</em></div><div class="view">View profile</div></div>
<div class="abs" style="left:843px;top:1712px;width:335px;text-align:center;font-size:20px;line-height:26px;color:var(--blue)">It's free to list your services on<br>brindlework.net</div>
<div class="abs small" style="left:850px;top:1778px">See the benefits</div>
<div class="abs btn" style="left:1045px;top:1770px;width:133px">List your services</div>

<!-- knowledge -->
<h3 class="abs col-title" style="left:902px;top:1808px">Knowledge Resource</h3>
<div class="abs" style="left:855px;top:1846px;font-size:16px;color:var(--blue)">Find resources for your busines s amongst</div>
<ul class="abs know" style="left:850px;top:1870px">
  <li>10,145 &nbsp;mar et analysis</li><li>9,254 &nbsp;business tips</li><li>3,215 &nbsp;agents and distributors</li><li>50,145 &nbsp;service providers</li>
</ul>
<div class="abs" style="left:850px;top:1994px;width:288px;height:44px;background:#fff;border:2px solid #8aa4c2;font-size:20px;color:var(--navy);padding:8px 12px">Select a country
  <span style="position:absolute;right:6px;top:7px;width:30px;height:26px;background:#6f93bf;display:flex;align-items:center;justify-content:center"><svg width="14" height="10" viewBox="0 0 14 10"><path d="M0 0h14L7 10z" fill="#fff"/></svg></span>
</div>
<div class="abs" style="left:1144px;top:1994px;width:44px;height:44px;background:var(--nav);color:#fff;font-size:22px;font-weight:700;display:flex;align-items:center;justify-content:center">OK</div>
<div class="abs" style="left:855px;top:2048px;font-size:20px;color:var(--blue)">Most popular :</div>
<div class="abs" style="left:855px;top:2084px;font-size:16px;line-height:32px;color:var(--blue);width:320px">China, &nbsp;Brazil, &nbsp;Japan, &nbsp;India, &nbsp;Egypt,<br>Korea, &nbsp;Angola, &nbsp;Italy, &nbsp;England, Spam,<br>China, &nbsp;Brazil, &nbsp;Japan, &nbsp;India, &nbsp;Egypt .</div>

<!-- partners -->
<div class="abs rule" style="left:40px;top:2210px;width:1120px"></div>
<div class="abs partners" aria-label="Partner organisations">
  <i style="width:118px;height:74px;border-radius:50%"></i>
  <i style="width:94px;height:70px"></i>
  <i style="width:190px;height:50px"></i>
  <i style="width:150px;height:56px"></i>
  <i style="width:168px;height:42px"></i>
  <i style="width:150px;height:70px"></i>
</div>
<div class="abs rule" style="left:40px;top:2342px;width:1120px"></div>

<!-- footer -->
<footer class="abs footer">
  <div class="fcol" style="left:40px"><h4>About</h4><p>About us<br>Partners<br>Site Map<br>Contact us<br>Terms &amp; Conditions<br>Privacy Policy</p></div>
  <div class="fcol" style="left:226px"><h4>Most Popular pages</h4><p>Distributors<br>Country Risk<br>Tax Law<br>Market Research<br>Business Development<br>Mergersand Acqisitions<br>Corparate Law</p><p class="sm">View all</p></div>
  <div class="fcol" style="left:454px"><h4>For Importers / Exporters</h4><p>Import Export Services<br>Trade Companies , Agents<br>Market Analysis Worldwide<br>International Business Tips<br>Receive Offers for Services</p><p class="sm">Take a tour</p></div>
  <div class="fcol" style="left:725px"><h4>For Service Providers</h4><p>Import Export Services<br>Trade Companies , Agents<br>Market Analysis Worldwide<br>International Business Tips<br>Receive Offers for Services</p><p class="sm">Take a tour</p></div>
  <div class="fcol follow" style="left:993px"><h4>Follow Us</h4>
    <p><i></i>Newsletter</p><p><i></i>Chirpline</p><p><i></i>RSS</p>
    <p style="padding-left:38px">Join Us</p><p><i></i>Friendspace</p><p><i></i>Linkfold</p>
  </div>
  <div class="copy">Brindlework.net - International Trade Resources, Import Export Services © 2012 All Rights Reserved.</div>
</footer>
</body>
</html>
```